Business Card Design Project

Use newly designed logo and tie into newly designed website
I need a new logo and website layout designed for my partner's business. This is a birthday present. His business is interior painting, wallpapering and design. He also has access to a wide variety of products including carpet, fabrics, furniture, wallpaper, tile, countertops, etc. I have attached some screen shots of his website for reference. He is a one man shop and has a stellar reputation with his customers. He is on-time, very tidy, excellent with animals, and always finishes on time and on budget. There are no restrictions on colors or fonts. The logo needs to work well with the website, business cards and printed materials. The website needs to flow content for device size so it looks just as good on a cell phone or tablet as it does on a desktop computer. Whatever the heck that's called!Thanks. I am looking forward to seeing everyone's ideas.
Updates
Hi Designers,
We've reopened this project as our logo design project has just completed.
Please refer to the uploaded files and make use of either Horizontal or Vertical versions of the logo depending on what you think is suitable for your design proposals.
We look forward to your creative submissions!
Target Market(s)
Consumers looking to improve the interior environment of their homes by updating wall paint or paper, flooring (either carpet, tile, or hardwoods), counter tops, window treatments, etc. Clients tend to be more upper middle class and have certain taste levels and expectations. New logo, website and business card should align to meet those levels.
Industry/Entity Type
Cell Phone
Look and feel
Each slider illustrates characteristics of the customer's brand and the style your logo design should communicate.

```html
<!DOCTYPE html>
<html lang="en">
<head>
<meta charset="utf-8">
<title>Bellamar Interior Designs — Business Card</title>
<link rel="stylesheet" href="https://fonts.googleapis.com/css2?family=Arimo:wght@700&display=swap">
<style>
  :root {
    --backdrop: #c9d5de;
    --card: #f7f7f8;
    --edge-red: #8e1b1f;
    --ink-navy: #1f1d3d;
    --ink-black: #141414;
    --accent-gold: #b39a62;
  }
  * { margin: 0; padding: 0; box-sizing: border-box; }
  html, body {
    width: 1200px;
    height: 840px;
    overflow: hidden;
    background: var(--backdrop);
  }
  .stage {
    position: relative;
    width: 1200px;
    height: 840px;
  }
  .business-card {
    position: absolute;
    left: 250px;
    top: 220px;
    width: 700px;
    height: 400px;
    background: var(--card);
    border-top: 10px solid var(--edge-red);
    border-bottom: 10px solid var(--edge-red);
    display: flex;
    flex-direction: column;
    align-items: center;
    justify-content: center;
    box-shadow: 0 10px 30px rgba(40, 60, 80, 0.18);
  }
  .brand {
    display: flex;
    align-items: center;
    gap: 16px;
    margin-top: -20px;
  }
  .brand-mark {
    width: 58px;
    height: 58px;
    background: var(--accent-gold);
  }
  .brand-name {
    font-family: "Arimo", Arial, sans-serif;
    font-weight: 700;
    font-size: 34px;
    line-height: 1.1;
    letter-spacing: 1px;
    color: var(--ink-navy);
    text-transform: uppercase;
  }
  .contact-line {
    margin-top: 34px;
    font-family: "Arimo", Arial, sans-serif;
    font-weight: 700;
    font-size: 17px;
    color: var(--ink-black);
  }
</style>
</head>
<body>
  <main class="stage">
    <section class="business-card">
      <div class="brand">
        <div class="brand-mark" aria-hidden="true"></div>
        <div class="brand-name">Bellamar<br>Interior Designs</div>
      </div>
      <p class="contact-line">24817 W Aspen Ct. • Lenexa, KS 66215 • (555) 314-2980</p>
    </section>
  </main>
</body>
</html>
```